Vantage Sport And Fitness- Rates

I am opening up a new Gym/Training Facility. The Name of my New gym is Vantage Sports And Fitness. I am wanting to design a card that captures Membership Pricing/Personal Training Pricing. I will Upload the Logo. My colors are Red/Black/Silver. I really want there pricing card to "POP". IT needs to be very Professional and Clean. I will be placing these cards on a 5'7 . I would like these item on the card:
Name of Company: Vantage Sports And Fitness
Address:
2817 Larkmoor Commerce Dr.
Suite 214 Chantilly, VA 20153
Phone #: 703-555-0187
website: www.vantagesnf-example.com
Membership Rates:
$99/Month
$49 Heroes Rate
Family Plan:
2 People $149
3 People $199
4 People $299
Personal Training Rates:
1 session $102
5 sessions $490
10 sessions $940
20 sessions $1,800
40 sessions $3,400
Please be creative

```html
<!DOCTYPE html>
<html lang="en">
<head>
<meta charset="utf-8">
<title>Vantage Sports And Fitness – Rates Card</title>
<link href="https://fonts.googleapis.com/css2?family=Montserrat:wght@400;500;600;700&display=swap" rel="stylesheet">
<style>
  :root {
    --red: #e3141e;
    --red-dark: #a80c12;
    --black: #0c0c0e;
    --charcoal: #1b1b1f;
    --silver-light: #f4f4f4;
    --silver: #c9c9cb;
    --silver-dark: #8e8e91;
    --white: #ffffff;
    --backdrop: #d6d6d8;
  }
  * { box-sizing: border-box; margin: 0; padding: 0; }
  html, body { width: 1200px; height: 687px; overflow: hidden; }
  body {
    background: var(--backdrop);
    font-family: "Montserrat", Arial, sans-serif;
    position: relative;
  }
  .rates-card {
    position: absolute;
    left: 366px;
    top: 13px;
    width: 446px;
    height: 630px;
    transform: scale(1.048);
    transform-origin: top left;
    background: var(--black);
    overflow: hidden;
    box-shadow: 0 8px 18px rgba(0,0,0,.25);
  }
  .athlete-photo {
    position: absolute;
    inset: 80px 0 50px 0;
    background:
      radial-gradient(ellipse at 70% 62%, #3a3032 0%, #1e1a1c 38%, transparent 70%),
      radial-gradient(ellipse at 22% 45%, #2a1416 0%, transparent 45%),
      linear-gradient(180deg, var(--charcoal), var(--black));
  }
  .brand-band { position: absolute; left: 0; top: 0; width: 446px; height: 82px; }
  .brand-name {
    position: absolute; left: 24px; top: 28px;
    color: var(--charcoal); font-weight: 600; font-size: 17px; line-height: 22px;
    white-space: nowrap;
  }

  .rate-box {
    position: absolute; left: 14px; width: 248px;
    border: 1.5px solid var(--red);
  }
  .rate-box.family { top: 143px; height: 137px; }
  .rate-box.training { top: 300px; height: 162px; }
  .rate-label {
    position: absolute; left: 70px; width: 137px;
    background: var(--red); color: var(--white);
    text-align: center; font-weight: 600; text-transform: uppercase;
  }
  .rate-label.family { top: 127px; height: 29px; font-size: 16px; line-height: 29px; }
  .rate-label.training { top: 292px; height: 29px; font-size: 10px; line-height: 11px; padding-top: 3px; }
  .rate-list { position: absolute; left: 36px; width: 222px; list-style: none; }
  .rate-list.family { top: 176px; }
  .rate-list.training { top: 340px; }
  .rate-list li {
    display: flex; justify-content: space-between;
    height: 22.5px; font-size: 12.5px; color: var(--white);
    text-transform: uppercase;
    border-bottom: 1px solid rgba(255,255,255,.06);
  }
  .rate-list .price { color: var(--red); width: 46px; text-align: left; }

  .promo { position: absolute; }
  .promo svg { position: absolute; left: 0; top: 0; }
  .promo-text {
    position: absolute; color: var(--white); font-weight: 700;
    text-align: center; text-transform: uppercase; line-height: 1.25;
  }
  .promo.membership { left: 274px; top: 118px; width: 160px; height: 110px; }
  .promo.membership .promo-text { left: 14px; top: 30px; width: 130px; font-size: 11.5px; }
  .promo.membership .promo-text strong { font-size: 14px; }
  .promo.heroes { left: 290px; top: 232px; width: 150px; height: 115px; }
  .promo.heroes .promo-text { left: 18px; top: 32px; width: 115px; font-size: 12px; }
  .promo.heroes .promo-text strong { display: block; font-size: 21px; margin-top: 4px; }

  .contact-bar { position: absolute; left: 0; top: 580px; width: 446px; height: 50px; }
  .address {
    position: absolute; left: 26px; top: 590px;
    color: var(--white); font-size: 11px; line-height: 14px; font-style: normal;
    display: flex; gap: 8px;
  }
  .phone-block { position: absolute; right: 12px; top: 586px; color: var(--white); text-align: left; }
  .phone { font-size: 16.5px; font-weight: 600; display: flex; align-items: center; gap: 6px; }
  .website { font-size: 10px; display: flex; align-items: center; gap: 6px; margin-top: 1px; }
</style>
</head>
<body>
  <article class="rates-card">
    <div class="athlete-photo" role="img" aria-label="Photo of a woman training on a leg press machine in a dark gym"></div>

    <svg class="brand-band" viewBox="0 0 446 82" aria-hidden="true">
      <defs>
        <linearGradient id="silverSheen" x1="0" y1="0" x2="1" y2="1">
          <stop offset="0" stop-color="#f7f7f7"/>
          <stop offset=".55" stop-color="#d7d7d9"/>
          <stop offset="1" stop-color="#9a9a9d"/>
        </linearGradient>
      </defs>
      <polygon points="0,0 366,0 288,78 0,78" fill="url(#silverSheen)"/>
      <polygon points="366,0 372,0 292,82 0,82 0,78 288,78" fill="#7d7d80"/>
    </svg>
    <p class="brand-name">Vantage Sports And Fitness</p>

    <div class="rate-box family"></div>
    <h2 class="rate-label family">Family Plan</h2>
    <ul class="rate-list family">
      <li><span>2 People</span><span class="price">$149</span></li>
      <li><span>3 People</span><span class="price">$199</span></li>
      <li><span>4 People</span><span class="price">$299</span></li>
    </ul>

    <div class="rate-box training"></div>
    <h2 class="rate-label training">Personal<br>Training Rates</h2>
    <ul class="rate-list training">
      <li><span>1 Session</span><span class="price">$102</span></li>
      <li><span>5 Sessions</span><span class="price">$490</span></li>
      <li><span>10 Sessions</span><span class="price">$940</span></li>
      <li><span>20 Sessions</span><span class="price">$1,800</span></li>
      <li><span>40 Sessions</span><span class="price">$3,400</span></li>
    </ul>

    <div class="promo membership">
      <svg width="160" height="110" viewBox="0 0 160 110" aria-hidden="true">
        <polygon points="6,6 130,0 130,92 6,86" fill="none" stroke="#fff" stroke-width="1.2"/>
        <polygon points="14,16 140,10 134,86 14,80" fill="var(--red)"/>
        <polygon points="14,80 34,80 24,94" fill="var(--red-dark)"/>
      </svg>
      <p class="promo-text">Membership<br>Rates:<br><strong>$99/Month</strong></p>
    </div>

    <div class="promo heroes">
      <svg width="150" height="115" viewBox="0 0 150 115" aria-hidden="true">
        <polygon points="10,4 140,22 140,90 10,110" fill="none" stroke="#fff" stroke-width="1.2"/>
        <polygon points="16,22 130,12 130,86 16,92" fill="var(--red)"/>
        <polygon points="110,86 130,86 124,100" fill="var(--red-dark)"/>
      </svg>
      <p class="promo-text">Heroes Rate:<strong>$49</strong></p>
    </div>

    <svg class="contact-bar" viewBox="0 0 446 50" aria-hidden="true">
      <rect width="446" height="50" fill="#000"/>
      <polygon points="270,0 446,0 446,50 244,50" fill="var(--red)"/>
    </svg>
    <address class="address">
      <svg width="10" height="14" viewBox="0 0 10 14" aria-hidden="true">
        <path d="M5 0a5 5 0 0 0-5 5c0 3.8 5 9 5 9s5-5.2 5-9a5 5 0 0 0-5-5zm0 7a2 2 0 1 1 0-4 2 2 0 0 1 0 4z" fill="var(--red)"/>
      </svg>
      <span>2817 Larkmoor Commerce Dr.<br>Suite 214 Chantilly, VA 20153</span>
    </address>
    <div class="phone-block">
      <p class="phone">
        <svg width="11" height="14" viewBox="0 0 11 14" aria-hidden="true">
          <path d="M3 0L0 1.5C0 8 4 13 9 14l2-3-3-2-1.5 1.5C5 9.5 3.5 7 3.5 5L5 4z" fill="#fff"/>
        </svg>703-555-0187</p>
      <p class="website">
        <svg width="9" height="9" viewBox="0 0 10 10" aria-hidden="true">
          <circle cx="5" cy="5" r="4.3" fill="none" stroke="#fff"/>
          <path d="M0.7 5h8.6M5 0.7v8.6" stroke="#fff"/>
        </svg>www.vantagesnf-example.com</p>
    </div>
  </article>
</body>
</html>
```